Mapping Bright Currents Through the Modern Seminar Room

This is for a book cover aimed at professors in higher education who want to infuse creative thinking into their classroom. It should have the title on the cover (see name of project). Our first idea is to have a stack of academic type books on a desk in black and white and then have a colorful rainbow light thread hitting the books. However, we are open to options! It has to be sophisticated, cool, and creative ;)

Target Market(s)

Higher Education Instructors

Industry/Entity Type

education

Font styles to use
Serif
Sans Serif

Requirements
Nice to have
• a creative feel of some sort
Should not have
• lightbulbs

```html
<!DOCTYPE html>
<html lang="en">
<head>
<meta charset="utf-8">
<title>Mapping Bright Currents Through the Modern Seminar Room</title>
<link href="https://fonts.googleapis.com/css2?family=Cormorant+Garamond:wght@500;600&family=Montserrat:wght@400&display=swap" rel="stylesheet">
<style>
  :root {
    --page: #ffffff;
    --cover-dark: #1c1c1d;
    --cover-fold: #242526;
    --title-white: #fbfaf6;
    --red: #e0563a;
    --orange: #f0a040;
    --yellow: #f3e27a;
    --green: #a9d98a;
    --blue: #6fb0d8;
    --violet: #b89ad0;
    --book-cream: #d9c49a;
    --book-red: #9c3a2c;
    --wood-light: #c98a4e;
    --wood-dark: #7a4322;
  }
  * { margin: 0; padding: 0; box-sizing: border-box; }
  html, body {
    width: 1200px; height: 1200px; overflow: hidden;
    background: var(--page);
  }
  .cover {
    position: absolute;
    left: 274px; top: 122px;
    width: 652px; height: 956px;
    overflow: hidden;
    background:
      repeating-linear-gradient(90deg, rgba(255,255,255,0) 0 60px, rgba(255,255,255,0.025) 60px 90px, rgba(255,255,255,0) 90px 150px),
      linear-gradient(180deg, var(--cover-fold), var(--cover-dark));
  }
  .light-beam {
    position: absolute;
    left: 232px; top: 0;
    width: 150px; height: 790px;
    background: linear-gradient(90deg,
      rgba(224,86,58,0) 0%, var(--red) 14%, var(--orange) 30%, var(--yellow) 46%,
      var(--green) 58%, var(--blue) 72%, var(--violet) 86%, rgba(184,154,208,0) 100%);
    -webkit-mask-image: linear-gradient(180deg, transparent 0%, rgba(0,0,0,0.5) 12%, rgba(0,0,0,0.85) 45%, rgba(0,0,0,0.8) 80%, rgba(0,0,0,0.45) 100%);
    mask-image: linear-gradient(180deg, transparent 0%, rgba(0,0,0,0.5) 12%, rgba(0,0,0,0.85) 45%, rgba(0,0,0,0.8) 80%, rgba(0,0,0,0.45) 100%);
    filter: blur(6px);
    opacity: 0.9;
  }
  .title-block {
    position: absolute;
    left: 47px; top: 88px;
    width: 560px;
  }
  .title {
    font-family: "Cormorant Garamond", "Times New Roman", serif;
    font-weight: 600;
    font-size: 84px;
    line-height: 88px;
    letter-spacing: 0.03em;
    text-transform: uppercase;
    background: linear-gradient(90deg,
      var(--title-white) 0%, var(--title-white) 30%, #f6d9a8 38%, #f3c36a 44%,
      #f2ecaa 50%, #bde3c4 54%, #a8cfe6 58%, #dcc4e6 64%, var(--title-white) 74%, var(--title-white) 100%);
    -webkit-background-clip: text;
    background-clip: text;
    color: transparent;
  }
  .subtitle {
    margin-top: 8px;
    font-family: "Montserrat", Arial, sans-serif;
    font-weight: 400;
    font-size: 18px;
    letter-spacing: 0.04em;
    text-transform: uppercase;
    background: linear-gradient(90deg,
      #e8e6e2 0%, #e8e6e2 50%, #f0b060 58%, #f3d98a 68%, #a8cfe6 75%, #e8e6e2 80%, #e8e6e2 100%);
    -webkit-background-clip: text;
    background-clip: text;
    color: transparent;
  }
  .book-stack {
    position: absolute;
    left: 179px; top: 502px;
    width: 297px; height: 416px;
    border-radius: 4px 4px 0 0;
    background: linear-gradient(180deg, #e6d6b4 0%, var(--book-cream) 22%, #b98f68 45%, var(--book-red) 75%, #a9503d 100%);
    opacity: 0.92;
  }
  .desk {
    position: absolute;
    left: 0; bottom: 0;
    width: 100%; height: 76px;
    background: linear-gradient(180deg, var(--wood-light) 0%, #b8743e 45%, var(--wood-dark) 100%);
  }
</style>
</head>
<body>
  <main class="cover">
    <div class="desk" role="img" aria-label="Wooden desk top"></div>
    <div class="book-stack" role="img" aria-label="Stack of old academic books with an open book fanned on top"></div>
    <div class="light-beam"></div>
    <header class="title-block">
      <h1 class="title">Mapping<br>Bright<br>Currents</h1>
      <p class="subtitle">Through the Modern Seminar Room</p>
    </header>
  </main>
</body>
</html>
```